Visitenkarten-Design für Steuerberater und Wirtschaftsprüfer
Zielgruppe
Steuerberater, Wirtschaftsprüfer in München
Aufgabenstellung
Wir haben ein Logo das uns gefällt, jetzt allerdings steht die Umfirmierung vor der Tür und aus der Kanzlei Wendeholt (so unser Name) wird Wendeholt und Partner mbB (die Jugend kommt mit als Partner in die Kanzlei) , Steuerberater, Wirtschaftsprüfer
Analog unseres alten Briefpapiers und der alten Visitenkarten soll eigentlich nur der Zusatz 'und Partner mbB' oder '& Partner mbB' gestaltet werden.
Das Dateiformat bei Visitenkarten bitte so übergeben, dass wir Namen selbst austauschen mit gängigen Officeprogrammen austauschen können. Bei den Visitenkarten ist das große 'Wendeholt' geprägt.
Ich stelle das Logo, das aktuelle Briefpapier und aktuelle Visitenkarten ein. Unsere Farbe ist grau.
Das Logo bitte in .pdf, .png, .psd und .eps (sagt mi alles nichts, haben wir aber alles schon mal irgendwo gebraucht) , Visiten karten auch in .pddf und .ai
Bei Fragen kontaktiert mich gern jederzeit.

```html
<!DOCTYPE html>
<html lang="de">
<head>
<meta charset="utf-8">
<title>Wendeholt &amp; Partner mbB – Visitenkarte</title>
<link href="https://fonts.googleapis.com/css2?family=Jost:wght@300;400&display=swap" rel="stylesheet">
<style>
  :root {
    --backdrop: #1e1e1e;
    --card: #5c5d5f;
    --emboss: #a4a4a4;
    --emboss-soft: #8c8c8d;
    --ink: #f4f4f4;
    --ink-muted: #c4c4c5;
    --rule: #ececec;
  }
  * { margin: 0; padding: 0; box-sizing: border-box; }
  html, body {
    width: 1101px; height: 1200px; overflow: hidden;
    background: var(--backdrop);
    font-family: "Jost", "Futura", sans-serif;
  }
  .card {
    position: absolute;
    background: var(--card);
    box-shadow: 0 2px 10px rgba(0,0,0,.45);
  }
  .card--front { left: 109px; top: 88px; width: 846px; height: 485px; }
  .card--back  { left: 109px; top: 613px; width: 850px; height: 485px; }

  .front-brand {
    position: absolute; left: 0; right: 0; top: 222px;
    text-align: center;
  }
  .front-brand .wordmark {
    font-weight: 400; font-size: 40px; letter-spacing: 3px;
    color: var(--emboss); line-height: 1;
  }
  .front-brand .tagline {
    margin-top: 26px;
    font-weight: 300; font-size: 24px; letter-spacing: .3px;
    color: var(--emboss-soft); line-height: 1;
  }

  .holder { position: absolute; left: 54px; top: 96px; color: var(--ink); }
  .holder .name { font-weight: 300; font-size: 39px; line-height: 1; }
  .holder .title {
    margin-top: 12px; font-weight: 300; font-size: 17.5px;
    line-height: 21px; color: var(--ink-muted);
  }

  .back-brand { position: absolute; right: 56px; top: 110px; text-align: right; }
  .back-brand .wordmark {
    font-weight: 400; font-size: 22px; letter-spacing: 1.5px;
    color: var(--ink); line-height: 1;
  }
  .back-brand .tagline {
    margin-top: 32px; font-weight: 300; font-size: 13.5px;
    color: var(--ink-muted); line-height: 1;
  }

  .rule {
    position: absolute; left: 48px; width: 754px; height: 2px;
    background: var(--rule);
  }
  .rule--top { top: 310px; }
  .rule--bottom { top: 445px; }

  .contact {
    position: absolute; top: 366px;
    display: flex; align-items: center; gap: 8px;
    color: var(--ink); font-size: 16px; font-weight: 400; line-height: 19px;
  }
  .contact svg { width: 20px; height: 20px; flex: none; }
  .contact .divider { width: 2px; height: 24px; background: var(--ink); flex: none; margin-right: 4px; }
  .contact--address { left: 43px; }
  .contact--phone { left: 320px; }
  .contact--web { left: 538px; }
</style>
</head>
<body>
  <section class="card card--front">
    <div class="front-brand">
      <div class="wordmark">WENDEHOLT &amp; PARTNER mbB</div>
      <div class="tagline">STEUERBERATER | WIRTSCHAFTSPRÜFER</div>
    </div>
  </section>

  <section class="card card--back">
    <div class="holder">
      <div class="name">Lukas F. Wendeholt</div>
      <div class="title">Dipl.-Kfm / Steuerberater<br>Wirtschaftsprüfer</div>
    </div>

    <div class="back-brand">
      <div class="wordmark">WENDEHOLT &amp; PARTNER mbB</div>
      <div class="tagline">STEUERBERATER | WIRTSCHAFTSPRÜFER</div>
    </div>

    <div class="rule rule--top"></div>

    <div class="contact contact--address">
      <svg viewBox="0 0 20 20" aria-hidden="true"><path d="M10 2 1 10h3v8h4.5v-5h3v5H16v-8h3z" fill="#f4f4f4"/></svg>
      <span class="divider"></span>
      <span>Lindenhofer Straße 22<br>80637 München</span>
    </div>

    <div class="contact contact--phone">
      <svg viewBox="0 0 20 20" aria-hidden="true"><path d="M5 2.5 7.5 6 6 8c1 2.5 3.2 4.8 6 6l2-1.5 3.5 2.5-1.5 2.5C10 17 3 10 2.6 4z" fill="none" stroke="#f4f4f4" stroke-width="1.4" stroke-linejoin="round"/></svg>
      <span class="divider"></span>
      <span>T&nbsp; 089 - 47 21 3300<br>F 089 - 47 21 3301</span>
    </div>

    <div class="contact contact--web">
      <svg viewBox="0 0 20 20" aria-hidden="true"><g fill="none" stroke="#f4f4f4" stroke-width="1.3"><circle cx="10" cy="10" r="8"/><ellipse cx="10" cy="10" rx="3.5" ry="8"/><path d="M2 10h16M3.2 6h13.6M3.2 14h13.6"/></g></svg>
      <span class="divider"></span>
      <span>info@kanzlei-wendeholt.com<br>www.kanzlei-wendeholt.com</span>
    </div>

    <div class="rule rule--bottom"></div>
  </section>
</body>
</html>
```